Envelope Design Project

I will need two envelopes to be designed:-

DL size
C4 size

Please see uploaded documents for Design specs:

1) Design specs provided by printer (doc called DL Envelope Specs)
2) Design specs to comply with Kestrel Mailways requirements (doc called Kestrel Mailways Envelope Design Requirements)

Please adhere to the above for final design. Many thanks.

Target Market(s)

Real Estate Agents, Strata Managers, Builders, Architects, Business Owners

Industry/Entity Type

Printer

Requirements
Must have
• In top left corner
- Logo
- Return address - Unit 8, 19 Wattlebark Rd, Marrowbay, NSW 2917

```html
<!DOCTYPE html>
<html lang="en">
<head>
<meta charset="utf-8">
<title>Corvane Asbestos &amp; Safety – DL and C4 Envelopes</title>
<link rel="stylesheet" href="https://fonts.googleapis.com/css2?family=Didact+Gothic&display=swap">
<style>
  :root {
    --bg-dark: #141414;
    --bg-mid: #3a3a3a;
    --bg-light: #6a6a6a;
    --paper: #ffffff;
    --ink: #2b2b2b;
    --ink-soft: #5a5a5a;
    --brand-green: #8cc63f;
    --brand-charcoal: #3c3c3c;
    --dieline: #d8d8d8;
  }
  * { margin: 0; padding: 0; box-sizing: border-box; }
  html, body { width: 1200px; height: 900px; overflow: hidden; }
  body {
    position: relative;
    font-family: "Didact Gothic", "Century Gothic", sans-serif;
    background:
      radial-gradient(ellipse 1000px 700px at 420px 0px, var(--bg-light) 0%, var(--bg-mid) 45%, var(--bg-dark) 100%);
  }
  .dielines { position: absolute; left: 0; top: 0; }
  .dielines path {
    fill: none;
    stroke: var(--dieline);
    stroke-width: 1;
    stroke-dasharray: 3 2;
  }
  .envelope-front {
    position: absolute;
    background: var(--paper);
    box-shadow: 0 1px 3px rgba(0,0,0,0.35);
  }
  .envelope-front--dl { left: 56px; top: 260px; width: 420px; height: 211px; }
  .envelope-front--c4 { left: 557px; top: 78px; width: 557px; height: 393px; }

  .accent-bar { position: absolute; top: 0; }
  .accent-bar--charcoal { background: var(--brand-charcoal); }
  .accent-bar--green { background: var(--brand-green); }

  .sender { position: absolute; color: var(--ink); }
  .sender__brand { display: flex; align-items: center; white-space: nowrap; }
  .sender__mark { background: var(--brand-green); flex: none; }
  .sender__name { color: var(--ink); line-height: 1; white-space: nowrap; }
  .sender__address { color: var(--ink-soft); line-height: 1.2; white-space: nowrap; }

  /* DL sizing */
  .envelope-front--dl .accent-bar--charcoal { left: 30px; width: 20px; height: 3px; }
  .envelope-front--dl .accent-bar--green { left: 55px; width: 36px; height: 3px; }
  .envelope-front--dl .sender { left: 30px; top: 16px; }
  .envelope-front--dl .sender__mark { width: 16px; height: 16px; margin-right: 5px; }
  .envelope-front--dl .sender__name { font-size: 9px; }
  .envelope-front--dl .sender__address { font-size: 6px; margin-top: 15px; }

  /* C4 sizing */
  .envelope-front--c4 .accent-bar--charcoal { left: 32px; width: 30px; height: 5px; }
  .envelope-front--c4 .accent-bar--green { left: 69px; width: 53px; height: 5px; }
  .envelope-front--c4 .sender { left: 32px; top: 25px; }
  .envelope-front--c4 .sender__mark { width: 28px; height: 28px; margin-right: 8px; }
  .envelope-front--c4 .sender__name { font-size: 14px; }
  .envelope-front--c4 .sender__address { font-size: 9.5px; margin-top: 15px; }
</style>
</head>
<body>
  <svg class="dielines" width="1200" height="900" viewBox="0 0 1200 900" aria-hidden="true">
    <path d="M56 260 L60 190 Q60 181 69 181 L463 181 Q472 181 472 190 L476 260"/>
    <path d="M56 262 L33 288 L30 455 L56 471"/>
    <path d="M476 262 L500 290 L502 455 L476 471"/>
    <path d="M56 471 L56 604 Q56 613 65 613 L467 613 Q476 613 476 604 L476 471"/>
    <path d="M557 78 L560 47 L1110 45 L1114 78"/>
    <path d="M557 78 L530 85 L526 460 L557 471"/>
    <path d="M1114 78 L1150 80 Q1195 84 1195 130 L1195 420 Q1195 468 1145 471 L1114 471"/>
    <path d="M557 471 L557 854 L1114 854 L1114 471"/>
  </svg>

  <section class="envelope-front envelope-front--dl" aria-label="DL envelope front">
    <span class="accent-bar accent-bar--charcoal"></span>
    <span class="accent-bar accent-bar--green"></span>
    <div class="sender">
      <div class="sender__brand">
        <span class="sender__mark"></span>
        <span class="sender__name">Corvane Asbestos &amp; Safety</span>
      </div>
      <p class="sender__address">Unit 8, 19 Wattlebark Rd<br>Marrowbay, NSW 2917</p>
    </div>
  </section>

  <section class="envelope-front envelope-front--c4" aria-label="C4 envelope front">
    <span class="accent-bar accent-bar--charcoal"></span>
    <span class="accent-bar accent-bar--green"></span>
    <div class="sender">
      <div class="sender__brand">
        <span class="sender__mark"></span>
        <span class="sender__name">Corvane Asbestos &amp; Safety</span>
      </div>
      <p class="sender__address">Unit 8, 19 Wattlebark Rd<br>Marrowbay, NSW 2917</p>
    </div>
  </section>
</body>
</html>
```